Agriculture new feeding concept for bull fattening needs a one-page flyer *

We are the innovation leader in the field of cattle feeding in Switzerland. Now we are launching a new “Tarsela” project for cattle fatteners, Munimäster (bull fattening). Tarsela is a complete fattening regime (feed, feed additives, services and advice).
Our sales representatives are with customers every day. You advertise the new project with the aim that our internal specialists get an appointment with the customer for a non-binding presentation of the project. This flyer is intended for this purpose.
Effect:
1. Innovative, modern
2. New
3. emotions
4. technical, scientific

You are also welcome to create a “logo” for Tarsela or choose / design your own lettering.
If you wish to use them, you will also find pictures of such fattening bulls in the appendix. However, pictures are not absolutely necessary.
Size A5, one-sided
Title: TARSELA - for beef fattening professionals
Text:
• Best fattening results
• Top customer service
• Innovative products
• Attractive conditions

Banner or similar:
May we introduce ourselves? or we would be happy to visit you. Etc.

```html
<!DOCTYPE html>
<html lang="en">
<head>
<meta charset="utf-8">
<title>Tarsela – for beef fattening professionals</title>
<link rel="stylesheet" href="https://fonts.googleapis.com/css2?family=Montserrat:wght@500;600;700;800&family=Nunito:wght@800;900&family=Arimo:wght@400&display=swap">
<style>
  :root{
    --page-bg:#8a8a8a;
    --green-mid:#566b4d;
    --green-light:#5b874b;
    --green-deep:#223b1e;
    --ink:#374a36;
    --ink-dark:#2e3b25;
    --white:#ffffff;
    --photo-warm:#9b5a30;
    --photo-cream:#e6dccd;
    --photo-steel:#b9bcbc;
    --photo-straw:#b79a62;
  }
  *{margin:0;padding:0;box-sizing:border-box;}
  html,body{width:1200px;height:848px;overflow:hidden;background:var(--page-bg);}
  .flyer{
    position:absolute;left:318px;top:24px;width:564px;height:800px;
    background:var(--white);overflow:hidden;
  }
  .flyer-shapes{position:absolute;inset:0;width:100%;height:100%;}
  .brand-mark{
    position:absolute;left:0;width:564px;top:112px;text-align:center;
    font-family:"Montserrat",sans-serif;font-weight:800;font-size:30px;
    letter-spacing:1px;color:var(--ink-dark);
  }
  .headline{
    position:absolute;left:0;width:564px;top:378px;text-align:center;
    font-family:"Montserrat",sans-serif;font-weight:700;font-size:80px;
    line-height:1;letter-spacing:-1px;color:var(--ink);
  }
  .tagline{
    position:absolute;left:0;width:564px;top:466px;text-align:center;
    font-family:"Arimo",sans-serif;font-size:26px;color:var(--ink);
  }
  .rule{
    position:absolute;left:78px;width:409px;top:514px;height:1.5px;background:var(--ink);
  }
  .benefits{position:absolute;left:35px;top:533px;list-style:none;}
  .benefit{
    display:flex;align-items:center;height:45px;
    font-family:"Nunito",sans-serif;font-weight:900;font-size:33px;
    letter-spacing:1px;color:var(--ink);
  }
  .benefit-icon{width:39px;height:39px;margin-right:11px;flex:none;}
  .invite{
    position:absolute;left:106px;top:724px;
    font-family:"Montserrat",sans-serif;font-weight:500;font-size:16.5px;
    line-height:23px;color:var(--ink);
  }
  .invite strong{font-weight:600;color:var(--green-light);}
</style>
</head>
<body>
<main class="flyer">
  <svg class="flyer-shapes" viewBox="0 0 922 1307" preserveAspectRatio="none">
    <rect class="header-band" x="0" y="0" width="922" height="255" fill="var(--green-mid)"/>
    <path class="brand-tab" d="M264,255 L264,225 A198,198 0 0 1 660,225 L660,255 Z" fill="var(--white)"/>
    <defs>
      <linearGradient id="photoLeft" x1="0" y1="0" x2="1" y2="1">
        <stop offset="0" stop-color="var(--photo-steel)"/>
        <stop offset="0.45" stop-color="var(--photo-warm)"/>
        <stop offset="0.75" stop-color="var(--photo-cream)"/>
        <stop offset="1" stop-color="var(--photo-straw)"/>
      </linearGradient>
      <linearGradient id="photoRight" x1="0" y1="0" x2="1" y2="1">
        <stop offset="0" stop-color="var(--photo-warm)"/>
        <stop offset="0.5" stop-color="var(--photo-cream)"/>
        <stop offset="0.8" stop-color="var(--photo-straw)"/>
        <stop offset="1" stop-color="var(--photo-cream)"/>
      </linearGradient>
    </defs>
    <polygon role="img" aria-label="Photo: Hereford fattening bulls feeding at a barn feed rail" points="0,254 506,254 418,592 0,592" fill="url(#photoLeft)"/>
    <polygon role="img" aria-label="Photo: young bulls eating feed along the barn feeding fence" points="522,254 922,254 922,595 432,595" fill="url(#photoRight)"/>
    <rect class="lower-band" x="0" y="592" width="922" height="715" fill="var(--green-mid)"/>
    <polygon points="0,592 95,592 13,787 0,680" fill="var(--green-light)"/>
    <polygon points="833,592 922,592 922,680 893,777" fill="var(--green-light)"/>
    <polygon points="0,680 13,787 0,822" fill="var(--green-deep)"/>
    <polygon points="922,680 893,777 922,862" fill="var(--green-deep)"/>
    <polygon class="content-panel" points="95,592 833,592 893,777 745,1307 68,1307 13,787" fill="var(--white)"/>
  </svg>

  <div class="brand-mark">TARSELA</div>

  <h1 class="headline">TARSELA</h1>
  <p class="tagline">for beef fattening professionals</p>
  <div class="rule"></div>

  <ul class="benefits">
    <li class="benefit">
      <svg class="benefit-icon" viewBox="0 0 40 40"><circle cx="20" cy="20" r="20" fill="var(--green-light)"/><path d="M20 10 L23 17 L30 17 L24.5 21.5 L26.5 29 L20 24.5 L13.5 29 L15.5 21.5 L10 17 L17 17 Z" fill="none" stroke="#fff" stroke-width="1.6" stroke-linejoin="round"/></svg>
      Best fattening results
    </li>
    <li class="benefit">
      <svg class="benefit-icon" viewBox="0 0 40 40"><circle cx="20" cy="20" r="20" fill="var(--green-light)"/><circle cx="15" cy="18" r="3.5" fill="#fff"/><path d="M9 30 a6 6 0 0 1 12 0 Z" fill="#fff"/><circle cx="26" cy="13" r="3.5" fill="none" stroke="#fff" stroke-width="1.6"/><path d="M21 25 a5 5 0 0 1 10 0 L31 26 L21 26 Z" fill="#fff"/></svg>
      Top customer service
    </li>
    <li class="benefit">
      <svg class="benefit-icon" viewBox="0 0 40 40"><circle cx="20" cy="20" r="20" fill="var(--green-light)"/><rect x="11" y="14" width="18" height="15" rx="1.5" fill="none" stroke="#fff" stroke-width="1.6"/><path d="M13 14 L15 10 L25 10 L27 14" fill="none" stroke="#fff" stroke-width="1.6"/><path d="M16 21.5 L19 24.5 L24 19" fill="none" stroke="#fff" stroke-width="1.6"/></svg>
      Innovative products
    </li>
    <li class="benefit">
      <svg class="benefit-icon" viewBox="0 0 40 40"><circle cx="20" cy="20" r="20" fill="var(--green-light)"/><path d="M8 20 Q20 9 32 20 Q20 31 8 20 Z" fill="none" stroke="#fff" stroke-width="1.6"/><circle cx="20" cy="20" r="4.5" fill="#fff"/></svg>
      Attractive conditions
    </li>
  </ul>

  <p class="invite">May we introduce <strong>ourselves?</strong><br>or we would be <strong>happy to visit you..</strong></p>
</main>
</body>
</html>
```